Morvell Agronomics, Inc. Business Card

We are joint venture hybrid vegetable seed company. We design & breed application specific products for fresh market and processing applications. We are looking for a business card that will have impact and convey elegance, excellence, high technology, and have enormous eye appeal. It needs to be unique in design and can incorporate photos, or symbols as the case may be.

I very much enjoy the minimalist approach to Quorin's product designs. We would like to include a tag line in the business card: Breeding Success

Target Market(s)

We breed proprietary products that provide better solutions for growers, harvesters, packers, shippers, wholesalers, retailers, consumers, and processors. Regional seed distributors worldwide are our primary clients and then growers. We need to appeal first and foremost to the distributors who will be representing us and selling the products in their target markets.

Industry/Entity Type

Business

Requirements
Must have
• It will have a picture of a cluster of tomatoes on one side and the other side will include the logo, a tag line, our contact information, and a possibly a picture or symbol. I want the contact side to be edgy and convey elegance, solidity, and exclusivity.
Nice to have
• Surprise us with something special.
Should not have
• Card needs to work well with the green logo so it can't be diminished by the background color of the card.

```html
<!DOCTYPE html>
<html lang="en">
<head>
<meta charset="utf-8">
<title>Morvell Agronomics, Inc. Business Card</title>
<link href="https://fonts.googleapis.com/css2?family=Arimo:wght@400;700&family=Varela+Round&display=swap" rel="stylesheet">
<style>
  :root {
    --stage: #ececec;
    --card: #ffffff;
    --green: #0f7a55;
    --green-dark: #0b4a35;
    --ink-gray: #6b6b6b;
    --soft-gray: #a9a9a9;
    --silver: #9a9a9a;
    --pattern-light: #e9e9e9;
    --pattern-mid: #c4c4c4;
    --tomato: #d6301b;
    --tomato-dark: #8f1a0e;
  }
  * { margin: 0; padding: 0; box-sizing: border-box; }
  html, body { width: 1200px; height: 900px; overflow: hidden; }
  body { background: var(--stage); position: relative; font-family: "Arimo", Arial, sans-serif; }

  .card {
    position: absolute;
    left: 262px;
    width: 670px;
    background: var(--card);
    border-radius: 4px;
    overflow: hidden;
    box-shadow: 0 3px 8px rgba(0,0,0,0.25);
  }
  .card--front { top: 35px; height: 392px; }
  .card--back { top: 468px; height: 390px; }
  .card__art { position: absolute; inset: 0; }

  .tagline {
    position: absolute;
    left: 0; right: 0; top: 98px;
    text-align: center;
    font-family: "Varela Round", Arial, sans-serif;
    font-size: 30px;
    color: var(--green);
    letter-spacing: 1px;
  }

  .brand {
    position: absolute;
    left: 0; right: 0;
    top: 181px;
    display: flex;
    align-items: center;
    justify-content: center;
    gap: 10px;
  }
  .brand__dot { width: 18px; height: 18px; border-radius: 50%; background: var(--green); }
  .brand__name {
    font-family: "Varela Round", Arial, sans-serif;
    font-size: 24px;
    color: var(--green);
  }

  .person { position: absolute; left: 20px; top: 251px; }
  .person__name { font-size: 19px; font-weight: 700; color: var(--green-dark); line-height: 24px; }
  .person__role { font-size: 17px; font-weight: 700; color: var(--green); line-height: 24px; }
  .person__links { margin-top: 12px; font-size: 18px; color: var(--green); line-height: 23px; letter-spacing: 0.4px; }

  .phones {
    position: absolute;
    left: 428px; top: 281px;
    font-size: 20px; color: var(--ink-gray); line-height: 24.5px;
  }
  .address {
    position: absolute;
    left: 0; right: 0; top: 360px;
    text-align: center;
    font-size: 17px; color: var(--soft-gray);
  }

  .back-name {
    position: absolute;
    left: 0; right: 0; top: 306px;
    text-align: center;
    font-family: "Varela Round", Arial, sans-serif;
    font-size: 38px;
    color: var(--silver);
  }
</style>
</head>
<body>

  <section class="card card--front" aria-label="Business card, contact side">
    <svg class="card__art" width="670" height="392" viewBox="0 0 670 392">
      <defs>
        <radialGradient id="frontPattern" cx="50%" cy="35%" r="65%">
          <stop offset="0" stop-color="#f4f4f4"/>
          <stop offset="1" stop-color="var(--pattern-mid)"/>
        </radialGradient>
        <linearGradient id="frontSwoosh" x1="0" x2="1">
          <stop offset="0" stop-color="#d4d4d4"/>
          <stop offset="0.5" stop-color="#f6f6f6"/>
          <stop offset="1" stop-color="#d4d4d4"/>
        </linearGradient>
      </defs>
      <rect role="img" aria-label="Grey seed-shape pattern background" width="670" height="270" fill="url(#frontPattern)"/>
      <path d="M0 182 Q335 300 670 182 L670 392 L0 392 Z" fill="url(#frontSwoosh)"/>
      <path d="M0 196 Q335 310 670 196 L670 392 L0 392 Z" fill="var(--card)"/>
    </svg>
    <p class="tagline">Breeding Success</p>
    <div class="brand">
      <span class="brand__dot"></span>
      <span class="brand__name">Morvell Agronomics, Inc.</span>
    </div>
    <div class="person">
      <p class="person__name">Daniel Harrow</p>
      <p class="person__role">CTO, CEO</p>
      <p class="person__links">Email: dan@morvellagronomics.com<br>Web: www.morvellagronomics.com</p>
    </div>
    <p class="phones">Tel: 01 555 214-3380<br>Cel: 01 555 307-6142<br>Fax: 01 555 468-9021</p>
    <p class="address">4720 Larkfield Ave. Fresno, CA 93711 USA</p>
  </section>

  <section class="card card--back" aria-label="Business card, image side">
    <svg class="card__art" width="670" height="390" viewBox="0 0 670 390">
      <defs>
        <radialGradient id="backPattern" cx="50%" cy="30%" r="65%">
          <stop offset="0" stop-color="#f4f4f4"/>
          <stop offset="1" stop-color="var(--pattern-mid)"/>
        </radialGradient>
        <radialGradient id="tomatoes" cx="45%" cy="45%" r="60%">
          <stop offset="0" stop-color="var(--tomato)"/>
          <stop offset="0.75" stop-color="#b8230f"/>
          <stop offset="1" stop-color="var(--tomato-dark)"/>
        </radialGradient>
        <linearGradient id="backSwoosh" x1="0" x2="1">
          <stop offset="0" stop-color="#d4d4d4"/>
          <stop offset="0.5" stop-color="#f6f6f6"/>
          <stop offset="1" stop-color="#d4d4d4"/>
        </linearGradient>
        <linearGradient id="plateRim" x1="0" x2="1">
          <stop offset="0" stop-color="var(--green)"/>
          <stop offset="0.6" stop-color="#0d6a49"/>
          <stop offset="1" stop-color="var(--green-dark)"/>
        </linearGradient>
      </defs>
      <rect role="img" aria-label="Grey seed-shape pattern background" width="670" height="230" fill="url(#backPattern)"/>
      <path d="M0 200 Q335 260 670 200 L670 390 L0 390 Z" fill="url(#backSwoosh)"/>
      <path d="M0 214 Q335 270 670 214 L670 390 L0 390 Z" fill="var(--card)"/>
      <ellipse cx="337" cy="222" rx="274" ry="58" fill="url(#plateRim)"/>
      <ellipse cx="330" cy="212" rx="226" ry="42" fill="#f2f2f2"/>
      <rect role="img" aria-label="Photo of a cluster of red vine tomatoes" x="138" y="10" width="406" height="228" rx="114" fill="url(#tomatoes)"/>
    </svg>
    <p class="back-name">Morvell Agronomics, Inc.</p>
  </section>

</body>
</html>
```